Mobile Dental services for School Students

I need a double sided letter/flyer designed to go to principals of schools about our services.
I have attached an example of a previous flyer done and would like something similar except with our other company logo and stock photos etc.

Please have a look at the word doc as this is the layout I want and the information that needs to be included on the flyer.
The colour scheme is orange, green, white, grey etc. Basically the colours of the dental truck photo.

Please see attachments as all these need to be incorporated into the flyer.

Target Market(s)

Schools, Principals

Industry/Entity Type

School

Font styles to use
Serif
Sans Serif

Colors
f37122
00a990
959595
ffffff
606060

Requirements
Must have
• Email, phone number, website, logo etc.

```html
<!DOCTYPE html>
<html lang="en">
<head>
<meta charset="utf-8">
<title>BrightVisit – School Flyer</title>
<link href="https://fonts.googleapis.com/css2?family=Quicksand:wght@500;700&family=Source+Sans+3:wght@400;600;700&display=swap" rel="stylesheet">
<style>
:root{
  --orange:#f37122;
  --green:#00a990;
  --grey:#959595;
  --dark:#606060;
  --ink:#4a4a4a;
  --white:#ffffff;
  --band:#d9eef5;
  --paper-top:#ffffff;
  --paper-bottom:#eaf5f8;
  --backdrop:#e4e4e4;
}
*{margin:0;padding:0;box-sizing:border-box}
html,body{width:1200px;height:1200px;overflow:hidden;background:var(--backdrop)}
body{position:relative;font-family:"Source Sans 3",Arial,sans-serif;color:var(--ink)}
.page{position:absolute;top:217px;width:542px;height:766px;overflow:hidden;
  background:linear-gradient(180deg,var(--paper-top) 30%,var(--paper-bottom) 100%);
  box-shadow:0 6px 18px rgba(0,0,0,.25)}
.page--front{left:42px}
.page--back{left:615px}
.hero{position:absolute;left:0;top:0;width:542px}
.brand{position:absolute;left:0;right:0;text-align:center;font-family:"Quicksand",sans-serif;
  font-weight:700;color:var(--green);letter-spacing:-.5px}
.brand span{background:var(--white);padding:0 10px;border-radius:6px}
.page--front .brand{top:308px;font-size:40px}
.page--back .brand{top:132px;font-size:40px}

.headline{position:absolute;left:0;right:0;top:388px;text-align:center;font-family:"Quicksand",sans-serif;
  font-weight:700;font-size:40px;color:var(--dark);letter-spacing:.5px}
.subhead{position:absolute;left:0;right:0;top:432px;text-align:center;font-family:"Quicksand",sans-serif;
  font-weight:700;font-size:28px;color:var(--orange)}
.quote-band{position:absolute;left:0;right:0;top:492px;height:59px;background:var(--band)}
.quote{position:absolute;left:33px;right:30px;top:500px;font-size:15.5px;line-height:20px;color:var(--ink)}
.qmark{position:absolute;font-family:Georgia,serif;font-weight:700;font-size:34px;color:var(--green);line-height:1}
.qmark--open{left:30px;top:478px}
.qmark--close{right:32px;top:532px}
.ref{position:absolute;left:0;right:0;top:554px;text-align:center;font-size:11px;color:var(--ink)}
.intro{position:absolute;left:33px;right:30px;top:591px;font-size:11.5px;line-height:15px}
.cta{position:absolute;left:0;right:0;text-align:center;font-family:"Quicksand",sans-serif;font-weight:700}
.cta--main{top:649px;font-size:22px;color:var(--green);letter-spacing:.4px}
.cta--sub{top:677px;font-size:15px;color:var(--orange)}

.letter{position:absolute;left:33px;right:32px;font-size:8px;line-height:11px;color:var(--ink)}
.letter p{margin-bottom:10px;text-align:justify}
.letter--top{top:231px}
.offer-title{position:absolute;left:0;right:0;top:354px;text-align:center;font-weight:700;font-size:10px;
  letter-spacing:1.5px;color:var(--orange)}
.offer-band{position:absolute;left:0;right:0;top:371px;height:89px;background:var(--band)}
.offers{position:absolute;top:375px;left:33px;right:32px;display:grid;grid-template-columns:1fr 1fr;column-gap:20px}
.offers ul{list-style:none}
.offers li{position:relative;padding-left:14px;font-size:8px;line-height:11px;margin-bottom:8px;text-align:justify}
.offers li svg{position:absolute;left:0;top:1px}
.letter--bottom{top:478px}
.signoff{position:absolute;right:32px;top:596px;text-align:right;font-size:8px}
.signoff .name{display:inline-block;margin-top:5px;border-top:1px solid #c8dde4;padding-top:4px}
.signoff strong{color:var(--orange);font-size:10.5px}
.booking{position:absolute;left:0;right:0;text-align:center;font-family:"Quicksand",sans-serif;font-weight:700}
.booking--1{top:652px;font-size:13px;color:var(--green)}
.booking--2{top:669px;font-size:17px;color:var(--orange)}
.booking--2 svg{vertical-align:-2px;margin:0 2px}

.footer{position:absolute;left:0;right:0;top:734px;height:24px;background:var(--green);
  display:flex;align-items:center;justify-content:space-around;padding:0 24px}
.footer::after{content:"";position:absolute;left:0;right:0;top:26px;height:6px;background:var(--orange)}
.contact{display:flex;align-items:center;gap:6px;color:var(--white);font-size:9px}
.contact .icon{width:28px;height:28px;border-radius:50%;background:var(--white);border:2px solid var(--green);
  box-shadow:0 0 0 1px var(--white);display:flex;align-items:center;justify-content:center}
</style>
</head>
<body>

<section class="page page--front">
  <svg class="hero" viewBox="0 0 542 400" height="400" aria-hidden="false">
    <defs>
      <linearGradient id="teensPhoto" x1="0" y1="0" x2="0" y2="1">
        <stop offset="0" stop-color="#ffffff"/>
        <stop offset=".45" stop-color="#e9d8c8"/>
        <stop offset="1" stop-color="#b9c6d3"/>
      </linearGradient>
    </defs>
    <rect role="img" aria-label="Photo of four smiling teenage students" x="0" y="0" width="542" height="400" fill="url(#teensPhoto)"/>
    <path d="M0,400 L0,378 C150,310 360,340 542,272 L542,400 Z" fill="#f3f9fb"/>
    <path d="M0,360 C150,290 360,320 542,258" fill="none" stroke="var(--orange)" stroke-width="7"/>
    <path d="M0,372 C150,302 360,332 542,268" fill="none" stroke="var(--white)" stroke-width="4"/>
    <path d="M0,380 C150,312 360,342 542,276" fill="none" stroke="var(--green)" stroke-width="6"/>
  </svg>
  <div class="brand"><span>BrightVisit</span></div>

  <h1 class="headline">OUR FOCUS IS ON</h1>
  <h2 class="subhead">Education and Prevention</h2>

  <div class="quote-band"></div>
  <span class="qmark qmark--open">&ldquo;</span>
  <p class="quote">1 in 5 children between the ages of 4-8 years of age will suffer from tooth decay or dental caries as a result of poor dental hygiene.</p>
  <span class="qmark qmark--close">&rdquo;</span>
  <p class="ref">Ref; The National Child Health Council</p>

  <p class="intro">Thus, leading to possible dental destruction to their adult teeth. This, in conjunction with diet, lifestyle and social welfare can be contribution to the increase of child absenteeism.</p>

  <p class="cta cta--main">BOOK OUR SERVICES NOW FOR 2018</p>
  <p class="cta cta--sub">and help us, Bring back your student's &ldquo;BRIGHT SMILE&rdquo;</p>

  <footer class="footer">
    <div class="contact"><span class="icon"><svg width="14" height="14" viewBox="0 0 14 14"><circle cx="7" cy="7" r="6" fill="none" stroke="#606060" stroke-width="1.2"/><ellipse cx="7" cy="7" rx="2.6" ry="6" fill="none" stroke="#606060" stroke-width="1"/><path d="M1 7h12M2 4h10M2 10h10" stroke="#606060" stroke-width=".9"/></svg></span>www.brightvisitdental.com.au</div>
    <div class="contact"><span class="icon"><svg width="14" height="14" viewBox="0 0 14 14"><path d="M3 1.5l2 .3 1 3-1.4 1.2a7 7 0 0 0 3.4 3.4L9.2 8l3 1 .3 2-1.7 1.5C6 12 2 8 1.5 3.2z" fill="#606060"/></svg></span>1800 555 014</div>
    <div class="contact"><span class="icon"><svg width="14" height="14" viewBox="0 0 14 14"><rect x="1.5" y="3" width="11" height="8" fill="none" stroke="#606060" stroke-width="1.2"/><path d="M1.5 3l5.5 4.5L12.5 3" fill="none" stroke="#606060" stroke-width="1.2"/></svg></span>hannah.m@brightvisitdental.com.au</div>
  </footer>
</section>

<section class="page page--back">
  <svg class="hero" viewBox="0 0 542 240" height="240">
    <defs>
      <linearGradient id="clinicPhoto" x1="0" y1="0" x2="1" y2="0">
        <stop offset="0" stop-color="#7d7d7d"/>
        <stop offset=".45" stop-color="#c9c9c9"/>
        <stop offset="1" stop-color="#a4a4a4"/>
      </linearGradient>
    </defs>
    <rect role="img" aria-label="Greyscale photo of a dental check-up and a smiling child" x="0" y="0" width="542" height="240" fill="url(#clinicPhoto)"/>
    <path d="M0,240 L0,222 C90,170 170,150 260,150 C380,150 450,140 542,112 L542,240 Z" fill="#f3f9fb"/>
    <path d="M0,205 C90,155 170,140 260,140 C380,140 450,128 542,100" fill="none" stroke="var(--orange)" stroke-width="6"/>
    <path d="M0,214 C90,164 170,148 260,148 C380,148 450,136 542,107" fill="none" stroke="var(--white)" stroke-width="3"/>
    <path d="M0,222 C90,172 170,156 260,156 C380,156 450,144 542,114" fill="none" stroke="var(--green)" stroke-width="5"/>
  </svg>
  <div class="brand"><span>BrightVisit</span></div>

  <div class="letter letter--top">
    <p>We thank you for the time you are taking to review our mobile dental service. Here at BrightVisit, we are committed to 'bring the dentist to you'.</p>
    <p>We are passionate about providing Bulked billed oral health care to all types of schools. We also service corporate companies, rural communities and aboriginal communities.</p>
    <p>Within Victoria, in the past year, we have serviced over 150 schools, and treated a total of 22,014 students so far.</p>
    <p>We are pleased to introduce our service designed to satisfy your student's dental needs. Our service is cost effective, user friendly and extremely beneficial in providing oral health education and prevention.</p>
  </div>

  <p class="offer-title">WE OFFER</p>
  <div class="offer-band"></div>
  <div class="offers">
    <ul>
      <li><svg width="9" height="9" viewBox="0 0 9 9"><circle cx="4.5" cy="4.5" r="3.8" fill="none" stroke="#f37122"/><path d="M2.6 4.6l1.3 1.3 2.5-2.6" fill="none" stroke="#f37122"/></svg>Free Bulked Billed and treatment to students who qualify for the Child Dental Benefits program; this includes a dental check-up, cleaning &amp; fluoride treatments, sealants, x-rays and fillings.</li>
      <li><svg width="9" height="9" viewBox="0 0 9 9"><circle cx="4.5" cy="4.5" r="3.8" fill="none" stroke="#f37122"/><path d="M2.6 4.6l1.3 1.3 2.5-2.6" fill="none" stroke="#f37122"/></svg>One-on-one oral health education from our professional dental clinicians.</li>
    </ul>
    <ul>
      <li><svg width="9" height="9" viewBox="0 0 9 9"><circle cx="4.5" cy="4.5" r="3.8" fill="none" stroke="#f37122"/><path d="M2.6 4.6l1.3 1.3 2.5-2.6" fill="none" stroke="#f37122"/></svg>Complimentary Dental care pack comprising of a toothbrush, toothpaste and other products.</li>
      <li><svg width="9" height="9" viewBox="0 0 9 9"><circle cx="4.5" cy="4.5" r="3.8" fill="none" stroke="#f37122"/><path d="M2.6 4.6l1.3 1.3 2.5-2.6" fill="none" stroke="#f37122"/></svg>Students also go into the draw to win various prices drawn after clinic's visit to the school.</li>
      <li><svg width="9" height="9" viewBox="0 0 9 9"><circle cx="4.5" cy="4.5" r="3.8" fill="none" stroke="#f37122"/><path d="M2.6 4.6l1.3 1.3 2.5-2.6" fill="none" stroke="#f37122"/></svg>Provide a referral to the student's regular dentist for further treatment they may require.</li>
    </ul>
  </div>

  <div class="letter letter--bottom">
    <p>BrightVisit operates within accepted best practice models, and as such, is familiar, and without exception complies with the relevant legislation, regulations, codes and guidelines governing dentistry, including but not limited to, the dental code of conduct for Health Practitioners by the National Dental Practice Board.</p>
    <p>Our mobile dental clinics feature state-of-the-art, oral health equipment and machinery. Including Digital x-rays systems that feature low dose radiation, as well as Australian Approved Child Safety standard wheel chair access. All BrightVisit dentists, oral therapists and hygienists are licenses with the national dental board and have their working with children checks.</p>
    <p>Thank you for considering BrightVisit, my team and I look forward to providing this free service to your school and most importantly,' bringing the dentist to you'.</p>
  </div>

  <div class="signoff">Kindest Regards,<br><span class="name"><strong>Hannah Mercer,</strong> Marketing Manager</span></div>

  <p class="booking booking--1">IF YOU WOULD LIKE TO BOOK THIS SERVICE FOR 2018</p>
  <p class="booking booking--2">PLEASE GIVE ME A CALL ON <svg width="15" height="15" viewBox="0 0 14 14"><path d="M3 1.5l2 .3 1 3-1.4 1.2a7 7 0 0 0 3.4 3.4L9.2 8l3 1 .3 2-1.7 1.5C6 12 2 8 1.5 3.2z" fill="none" stroke="#f37122" stroke-width="1.2"/></svg> 0400 555 218</p>

  <footer class="footer">
    <div class="contact"><span class="icon"><svg width="14" height="14" viewBox="0 0 14 14"><circle cx="7" cy="7" r="6" fill="none" stroke="#606060" stroke-width="1.2"/><ellipse cx="7" cy="7" rx="2.6" ry="6" fill="none" stroke="#606060" stroke-width="1"/><path d="M1 7h12M2 4h10M2 10h10" stroke="#606060" stroke-width=".9"/></svg></span>www.brightvisitdental.com.au</div>
    <div class="contact"><span class="icon"><svg width="14" height="14" viewBox="0 0 14 14"><path d="M3 1.5l2 .3 1 3-1.4 1.2a7 7 0 0 0 3.4 3.4L9.2 8l3 1 .3 2-1.7 1.5C6 12 2 8 1.5 3.2z" fill="#606060"/></svg></span>1800 555 014</div>
    <div class="contact"><span class="icon"><svg width="14" height="14" viewBox="0 0 14 14"><rect x="1.5" y="3" width="11" height="8" fill="none" stroke="#606060" stroke-width="1.2"/><path d="M1.5 3l5.5 4.5L12.5 3" fill="none" stroke="#606060" stroke-width="1.2"/></svg></span>hannah.m@brightvisitdental.com.au</div>
  </footer>
</section>

</body>
</html>
```